New layout on letterheads, businesscards, flyers, brochures etc.

Dear Sir,
We would like to change our layout a bit. We would like to have the same look on everything we make and still keep our logo. We would like some suggestions suitable for a company like ours, where solar systems, heat pumps and LED lighting is reflected. We like our blue colour in our logo (#009ddf) and some of the black reflected in our solar panels and we like the solar cell (almost square with soft corners). We like soft lines, clean look and reflecting expensive solar panels from the very best distributors (RV, Korvantaku, Umbra Kestrel etc.). We want a light, soft, exclusive and expensive look to it all. We need this for business cards, letterhead/bottom, flyers, brochures and stickers etc.
Thank you in advance.

Tavix
Holmvej 38 B
8615 Ikast
Denmark

info@tavix-energi.dk
www.tavix-energi.dk

```html
<!DOCTYPE html>
<html lang="da">
<head>
<meta charset="utf-8">
<title>Tavix – brevpapir</title>
<link rel="stylesheet" href="https://fonts.googleapis.com/css2?family=Inter:wght@400;500;700&display=swap">
<style>
  :root {
    --paper: #ffffff;
    --ink: #111111;
    --header-ink: #3a3a3a;
    --brand-blue: #009ddf;
    --sun-light: #fbe3a2;
    --sun-warm: #ecb27e;
    --panel-mid: #6e6f8a;
    --panel-dark: #3b4462;
  }
  html, body {
    margin: 0;
    padding: 0;
    width: 848px;
    height: 1200px;
    overflow: hidden;
    background: var(--paper);
  }
  .letterhead {
    position: relative;
    width: 848px;
    height: 1200px;
    background: var(--paper);
    font-family: "Inter", Arial, sans-serif;
    color: var(--ink);
  }
  .header-band {
    position: absolute;
    left: 21px;
    top: 21px;
    width: 807px;
    height: 221px;
    overflow: hidden;
  }
  .header-photo {
    position: absolute;
    inset: 0;
    background:
      radial-gradient(ellipse at 8% 20%, rgba(255,248,220,0.9) 0%, rgba(255,248,220,0) 45%),
      linear-gradient(100deg, var(--sun-light) 0%, var(--sun-warm) 32%, var(--panel-mid) 55%, var(--panel-dark) 100%);
  }
  .brand {
    position: absolute;
    left: 19px;
    top: 22px;
    display: flex;
    align-items: center;
    gap: 12px;
  }
  .brand-mark {
    width: 30px;
    height: 30px;
    border-radius: 7px;
    background: var(--brand-blue);
  }
  .brand-name {
    font-size: 60px;
    font-weight: 700;
    line-height: 1;
    color: var(--brand-blue);
    letter-spacing: 1px;
  }
  .sender-contact {
    position: absolute;
    left: 19px;
    top: 150px;
    margin: 0;
    font-size: 14px;
    line-height: 19px;
    font-weight: 400;
    color: var(--header-ink);
    font-style: normal;
  }
  .fold-mark {
    position: absolute;
    left: 0;
    top: 400px;
    width: 12px;
    height: 1px;
    background: var(--ink);
  }
  .letter-body {
    position: absolute;
    left: 121px;
    top: 371px;
    width: 620px;
    font-size: 15px;
    line-height: 21.7px;
  }
  .letter-body p {
    margin: 0 0 11.5px;
  }
  .recipient, .closing, .signature {
    font-weight: 500;
  }
</style>
</head>
<body>
  <div class="letterhead">
    <header class="header-band">
      <div class="header-photo" role="img" aria-label="Photograph of sunlit solar panels, warm golden light on the left fading into dark blue panels on the right"></div>
      <div class="brand">
        <span class="brand-name">Tavix</span>
        <span class="brand-mark"></span>
      </div>
      <address class="sender-contact">
        Holmvej 38 B, 8615 Ikast, Denmark<br>
        P +45 70 31 52 84<br>
        info@tavix-energi.dk&nbsp; www.tavix-energi.dk
      </address>
    </header>

    <div class="fold-mark"></div>

    <main class="letter-body">
      <p>Vælg en dokumentkomponent.</p>
      <p class="recipient">
        Virksomhed eller navn<br>
        Gade x<br>
        xxxx By<br>
        Land<br>
        evt. Att.: xxx xxxxxxxx
      </p>
      <p class="date">Ikast, Klik her for at angive en dato.</p>
      <p class="salutation">Kære Kunde/forhandler</p>
      <p>Du skal endnu en gang have mange tak for din henvendelse, som aftalt sender jeg dig her yderligere informationer.</p>
      <p>Hvis du har nogen spørgsmål er du velkommen til at kontakte mig på tlf.: 70 31 52 84 eller på mail via info@tavix-energi.dk, så vil jeg hurtigst muligt vende tilbage med et svar.</p>
      <p class="closing">Med venlig hilsen</p>
      <p class="signature">Afsender</p>
    </main>
  </div>
</body>
</html>
```